Automotive component supplier needs a business card design

We need a business card design for our company called Velmar Global Components Ltd based in the UK. We are a supplier of interior and exterior components to premium car manufacturers such as Corvane Hale, Durrant Fyfe, Maxtorn and Valdessimo. We would like to see a modern business card design that uses the colour blue.

Target Market(s)

Premium automotive car manufacturers.

Industry/Entity Type

Automotive

Contact Information for Business Card

Company Name : Velmar Global Components Limited
Address: 17 Tamsey Yard, Upper Drisk, Warwick, CV31 8RJ, United Kingdom
Web Address : www.velmarparts-example.co.uk

Font styles to use
Other font styles liked:
• Helvetica

Colors
3176b5
0255a3
85acd3
cfdeed
cee9f5
85cae6
34a6d7
0692cd
9bcb3c

Requirements
Must have
• Clear company logo and a mixture of blue colours.
Nice to have
• A high quality modern image.
Should not have
• Multiple colours.

```html
<!DOCTYPE html>
<html lang="en">
<head>
<meta charset="utf-8">
<title>Velmar Global Components – Business Card</title>
<link rel="stylesheet" href="https://fonts.googleapis.com/css2?family=Open+Sans:wght@400;600&family=Oswald:wght@500&display=swap">
<style>
  :root {
    --stage: #e9edf1;
    --card-blue: #0a96d4;
    --map-blue: #34a6d7;
    --white: #ffffff;
    --ink: #1b1b1b;
    --accent-blue: #0692cd;
  }
  * { box-sizing: border-box; margin: 0; padding: 0; }
  html, body {
    width: 1200px; height: 1000px; overflow: hidden;
    background: var(--stage);
    font-family: "Open Sans", Arial, sans-serif;
  }
  .canvas { position: relative; width: 1200px; height: 1000px; }
  .card {
    position: absolute; left: 266px; width: 666px; height: 397px;
    border-radius: 24px; overflow: hidden;
    box-shadow: 0 3px 10px rgba(0,0,0,0.18);
  }
  .card-front { top: 74px; background: var(--card-blue); }
  .card-back { top: 534px; background: var(--white); }

  .world-map-area {
    position: absolute; left: 40px; top: 18px; width: 600px; height: 370px;
    border-radius: 40px;
    background: radial-gradient(ellipse at 50% 45%, rgba(52,166,215,0.9), rgba(52,166,215,0) 72%);
  }
  .brand {
    position: absolute; left: 0; right: 0; top: 140px;
    text-align: center; color: var(--white); font-weight: 600;
  }
  .brand-name {
    font-size: 80px; line-height: 84px; letter-spacing: 2px;
  }
  .brand-sub {
    font-size: 20px; letter-spacing: 7.5px; margin-top: 2px; padding-left: 7.5px;
  }
  .front-web {
    position: absolute; left: 0; right: 0; top: 348px;
    text-align: center; color: var(--white); font-size: 16px;
  }

  .person {
    position: absolute; right: 357px; top: 170px; text-align: right;
  }
  .person-name {
    font-family: "Oswald", "Arial Narrow", sans-serif; font-weight: 500;
    font-size: 29px; line-height: 32px; color: var(--accent-blue); letter-spacing: 0.5px;
  }
  .person-role { font-size: 16px; color: var(--ink); line-height: 22px; }
  .divider {
    position: absolute; left: 332px; top: 159px; width: 2px; height: 80px; background: var(--ink);
  }
  .contact-list { position: absolute; left: 356px; top: 150px; list-style: none; }
  .contact-list li {
    display: flex; align-items: center; gap: 6px;
    font-size: 16px; line-height: 23px; color: var(--ink);
  }
  .contact-list svg { width: 15px; height: 15px; fill: var(--accent-blue); flex: none; }
  .address {
    position: absolute; left: 0; right: 0; top: 345px;
    text-align: center; font-size: 16px; color: var(--ink);
  }
</style>
</head>
<body>
<main class="canvas">
  <section class="card card-front">
    <div class="world-map-area" role="img" aria-label="Faint world map across the card background"></div>
    <div class="brand">
      <div class="brand-name">VELMAR</div>
      <div class="brand-sub">GLOBAL COMPONENTS</div>
    </div>
    <p class="front-web">www.velmarparts-example.co.uk</p>
  </section>

  <section class="card card-back">
    <div class="person">
      <p class="person-name">TAVREN OSKAL</p>
      <p class="person-role">Vice President</p>
    </div>
    <div class="divider"></div>
    <ul class="contact-list">
      <li><svg viewBox="0 0 16 16" aria-hidden="true"><path d="M2 6c0-2 3-3 6-3s6 1 6 3v1h-3V5.5C10 5 6 5 5 5.5V7H2z"/><path d="M4 8h8l2 5H2z"/></svg>+ 000 000 0000</li>
      <li><svg viewBox="0 0 16 16" aria-hidden="true"><rect x="4" y="1" width="8" height="4"/><rect x="1" y="6" width="14" height="6" rx="1"/><rect x="4" y="10" width="8" height="5" fill="#fff" stroke="#0692cd"/></svg>+ 000 000 0000</li>
      <li><svg viewBox="0 0 16 16" aria-hidden="true"><rect x="1" y="3" width="14" height="10"/><path d="M1 3l7 6 7-6" fill="none" stroke="#fff" stroke-width="1.4"/></svg>info@velmarparts-example.co.uk</li>
      <li><svg viewBox="0 0 16 16" aria-hidden="true"><circle cx="8" cy="8" r="7"/><path d="M1 8h14M8 1c-3 3-3 11 0 14M8 1c3 3 3 11 0 14" fill="none" stroke="#fff" stroke-width="1"/></svg>www.velmarparts-example.co.uk</li>
    </ul>
    <p class="address">17 Tamsey Yard, Upper Drisk, Warwick, CV31 8RJ, United Kingdom</p>
  </section>
</main>
</body>
</html>
```